Retail Product Label Design

We need a 4" w X 3" h label. The label will be applied to a stand up zip lock clear poly bag. 2" at the bottom of the bag will remain clear as a window to the product. The product is small packs of minerals that are placed in fruit, vegetable and flower storage. please go to www.pouchpalio.com for more info. We are thinking a green color with fruits and vegetables included similar to what we use now (see attached file). We would like to consider a retro-style (bright colors almost cartoonish like the labels on Tolvan's Taproom Beer Labels and glasses. We have exact specs for the layout when necessary. They can be found @ http://www.wrapkinmart.com/images/main/wkm-label-requirements.pdf. We would also like to freshen up our logo (see attached file). This will be one of possibly 3 labels. One label will focus on fruits and vegetables, one will focus on flowers and one will focus on valuables like electronics, cameras and silver jewelry. Colors should be limited to 5 or possibly 6.
Target Market(s)
Grocery store fruit and vegetable buyers
Industry/Entity Type
Electronics
Look and feel
Each slider illustrates characteristics of the customer's brand and the style your logo design should communicate.

```html
<!DOCTYPE html>
<html lang="en">
<head>
<meta charset="utf-8">
<title>PouchPalio – Keep produce fresh longer</title>
<link rel="stylesheet" href="https://fonts.googleapis.com/css2?family=Roboto+Condensed:wght@700&family=Open+Sans:wght@700&family=Arimo:wght@400;700&display=swap">
<style>
  :root {
    --leaf: #3fae2a;
    --leaf-light: #8ed63a;
    --leaf-deep: #1f7a1f;
    --forest: #0b5a22;
    --forest-dark: #07461a;
    --panel: rgba(170, 225, 110, 0.9);
    --ink-green: #0d5a1f;
    --sun: #f4f000;
    --white: #ffffff;
  }
  * { margin: 0; padding: 0; box-sizing: border-box; }
  html, body { width: 1200px; height: 909px; overflow: hidden; background: var(--white); }
  .label {
    position: relative;
    width: 1200px;
    height: 909px;
    overflow: hidden;
    background:
      repeating-conic-gradient(from 0deg at 640px 260px, rgba(255,255,255,0.07) 0deg 6deg, rgba(0,0,0,0) 6deg 12deg),
      radial-gradient(circle at 640px 260px, var(--leaf-light) 0%, var(--leaf) 45%, var(--leaf-deep) 100%);
    font-family: "Open Sans", Arial, sans-serif;
    font-weight: 700;
  }
  .corner-flag {
    position: absolute;
    top: 0; right: 0;
    width: 1200px; height: 909px;
  }
  .corner-text {
    position: absolute;
    top: 62px; right: -14px;
    width: 340px;
    transform: rotate(33deg);
    transform-origin: center;
    text-align: center;
    color: var(--sun);
    font-family: "Roboto Condensed", Arial, sans-serif;
    font-weight: 700;
    font-size: 42px;
    line-height: 1.02;
  }
  .brand {
    position: absolute;
    left: 48px; top: 40px;
    width: 255px;
    display: flex; flex-direction: column; align-items: center;
  }
  .brand-mark {
    width: 220px; height: 220px;
    background: var(--white);
    border-radius: 34px;
  }
  .brand-name {
    margin-top: 42px;
    font-family: "Arimo", Arial, sans-serif;
    font-weight: 700;
    font-size: 42px;
    color: var(--white);
  }
  .headline {
    position: absolute;
    left: 360px; top: 70px;
    font-family: "Roboto Condensed", Arial, sans-serif;
    font-weight: 700;
    font-size: 86px;
    line-height: 80px;
    color: var(--white);
    -webkit-text-stroke: 3px var(--forest);
    paint-order: stroke fill;
    text-shadow: 3px 3px 0 var(--forest);
  }
  .headline .line-two { display: block; padding-left: 232px; }
  .subhead {
    position: absolute;
    left: 355px; top: 264px;
    font-size: 31px;
    font-weight: 700;
    color: var(--white);
  }
  .produce {
    position: absolute;
    left: 0; top: 410px;
    width: 1200px; height: 390px;
    border-radius: 160px 220px 0 0;
    background: linear-gradient(90deg, #f2b21a 0%, #e8541c 25%, #f08a14 45%, #d8321c 65%, #e87a18 85%, #f0c240 100%);
  }
  .claims {
    position: absolute;
    left: 95px; top: 652px;
    width: 760px; height: 142px;
    background: var(--panel);
    border-radius: 40px 40px 0 0;
    display: flex; align-items: center; justify-content: center;
    text-align: center;
    color: var(--ink-green);
    font-size: 27px;
    font-weight: 700;
    line-height: 40px;
  }
  .net-weight {
    position: absolute;
    left: 903px; top: 686px;
    width: 190px; height: 108px;
    background: var(--panel);
    border-radius: 32px 32px 0 0;
    display: flex; align-items: center; justify-content: center;
    text-align: center;
    color: var(--ink-green);
    font-size: 23px;
    font-weight: 700;
    line-height: 30px;
  }
  .footer-band {
    position: absolute;
    left: 0; top: 794px;
    width: 1200px; height: 115px;
    background: linear-gradient(180deg, var(--forest) 0%, var(--forest-dark) 100%);
    display: flex; flex-direction: column; align-items: center; justify-content: center;
    color: var(--white);
    font-family: "Arimo", Arial, sans-serif;
    font-size: 26px;
    line-height: 34px;
  }
  .footer-band strong { font-weight: 700; }
  .footer-band .light { font-weight: 400; }
</style>
</head>
<body>
<main class="label">
  <svg class="corner-flag" viewBox="0 0 1200 909" aria-hidden="true">
    <polygon points="735,0 1200,0 1200,300" fill="#0b5a22"/>
  </svg>
  <div class="corner-text">NEW<br>6 Month Supply</div>

  <div class="brand">
    <div class="brand-mark"></div>
    <div class="brand-name">PouchPalio</div>
  </div>

  <h1 class="headline">Keep produce<span class="line-two">fresh longer...</span></h1>
  <p class="subhead">with NO special bags and containers!</p>

  <div class="produce" role="img" aria-label="Photograph of assorted fresh fruits and vegetables: peppers, tomatoes, bananas, pineapple, apples, onions and lettuce"></div>

  <p class="claims">Extend the life of fruits, vegetables,<br>cheeses, bread, cereal, snacks, plant products.</p>
  <p class="net-weight">Net Wt:<br>60g (2.1 oz)<br>6 Packets</p>

  <footer class="footer-band">
    <p><strong>Better for your wallet –</strong> <span class="light">use over and over again!</span></p>
    <p><strong>BETTER for the environment –</strong> <span class="light">safe and natural, no unfriendly plastic</span></p>
  </footer>
</main>
</body>
</html>
```